Kestrel leadership hierchy redesign

Hi there, you created an awesome graphic design a while back. In our martial arts organization, elements are used to indicate an individuals leadership level and authority.
You start with a white uniform (black kestrel logos) and earn three different collars like a rising sun....
Purple, then Orange, Then Yellow.
After a student earns yellow collar....they will earn elemental logos on their black belt. We use to do colored collars for the wind, water, fire, and earth leadership levels but now we want to simplfy everything and put a colored hexagonal element logo in their black belt.
So after an individual earns a yellow collar.....
Their next goal is to either become a Program Director (Water) or a Lead Instructor (Wind)
For the Water Element, there are 4 levels you could earn as a logo on your black belt
Level 1 would be a Royal Blue hexagon outlined in white with our water symbol in the middle in white. Also label it with the rules to earn it: 50 Active Students
Level 2 would be a Royal Blue hexagon outlined in black with our water symbol in the middle in black.
Also label it with the rules to earn it: 100 Active Students
Level 3 would be a Royal Blue hexagon outlined in silver with our water symbol in the middle in silver.
Also label it with the rules to earn it: 150 Active Students.
Level 4 would be a Royal Blue hexagon outlined in silver with our water symbol in the middle in silver.
Also label it with the rules to earn it: 200
Active Students.
Chief Instructor Leadership Level (Fire) will follow the same guidelines as 4 level concept as water. Just change out water for fire and change out
Blue for red.
For Lead Instructor Wind , its only 1 level
Should be a white hexagon with a black outline and black wind symbol.
Final one, earth should be on top because its the hardest to obtain leadership wise. Same 4 levels as water and fire but the leadership requirements are diffrent.
Level 1 for earth
200 Active Students and 3 Active instructors who've earned elements.
Level 2 for earth
350 Active Students and 6 Active instructors who've earned elements.
Level 3 for earth
500 Active Students and 9 Active instructors who've earned elements.
Level 4 for earth
1000 Active Students and 18 Active instructors who've earned elements.
Label the graphic design with
Ignite Kestrel Path (on the bottom)
Serve Beyond Yourself (at the top)
Also i uploaded my belt posters so you dan gry to match the black/white/gold aethstetic. But please do elemental colored boxes like you did before in your previous design

```html
<!DOCTYPE html>
<html lang="en">
<head>
<meta charset="utf-8">
<title>Kestrel Leadership Hierchy</title>
<link href="https://fonts.googleapis.com/css2?family=Black+Ops+One&family=Cinzel:wght@400;500&family=Montserrat:wght@400;500;700&display=swap" rel="stylesheet">
<style>
  :root {
    --bg: #050505;
    --gold: #e0a23a;
    --gold-light: #f6dc8e;
    --gold-deep: #c9771f;
    --rule: #8a6a2a;
    --white: #f4f4f4;
    --silver: #c9c9c9;
    --fire: #b3120f;
    --fire-text: #9b1512;
    --water: #2a2fa8;
    --water-text: #3a3fc4;
  }
  * { margin: 0; padding: 0; box-sizing: border-box; }
  html, body { width: 800px; height: 1200px; overflow: hidden; background: var(--bg); }
  .canvas { position: relative; width: 800px; height: 1200px; background: var(--bg); color: var(--white); font-family: "Montserrat", sans-serif; }

  .tagline { position: absolute; top: 42px; left: 0; width: 800px; text-align: center; font-family: "Cinzel", serif; font-size: 16px; letter-spacing: 0.5px; color: var(--white); }
  .title { position: absolute; top: 70px; left: 0; width: 800px; text-align: center; font-family: "Black Ops One", sans-serif; font-size: 31px; letter-spacing: 0.5px;
    background: linear-gradient(180deg, var(--gold-light) 0%, var(--gold) 45%, var(--gold-deep) 100%); -webkit-background-clip: text; background-clip: text; color: transparent; }

  .timeline { position: absolute; left: 79px; top: 145px; width: 2px; height: 912px; background: linear-gradient(180deg, rgba(255,255,255,0) 0%, #e8e8e8 8%, #e8e8e8 92%, rgba(255,255,255,0) 100%); }
  .node { position: absolute; left: 0; width: 140px; height: 0; }
  .node-num { position: absolute; left: 30px; top: -11px; font-family: "Cinzel", serif; font-size: 17px; color: var(--white); }
  .node-diamond { position: absolute; left: 69px; top: -11px; width: 22px; height: 22px; transform: rotate(45deg); background: linear-gradient(135deg, #ffffff 0%, #cfcfcf 50%, #7a7a7a 100%); box-shadow: 0 0 6px rgba(255,255,255,0.4); }
  .node-tick { position: absolute; left: 95px; top: -1px; width: 45px; height: 2px; background: linear-gradient(90deg, #f0f0f0, rgba(255,255,255,0)); }

  .rule { position: absolute; left: 82px; width: 682px; height: 1px; background: linear-gradient(90deg, rgba(138,106,42,0.3), var(--rule) 30%, var(--rule) 70%, rgba(138,106,42,0.3)); }

  .badge { position: absolute; }
  .badge svg { display: block; width: 100%; height: 100%; }

  .tier-name { position: absolute; font-family: "Black Ops One", sans-serif; line-height: 1; }
  .tier-role { position: absolute; font-family: "Cinzel", serif; color: var(--white); line-height: 1; }

  .earth-name { left: 338px; top: 160px; font-size: 29px; background: linear-gradient(180deg, var(--gold-light), var(--gold) 50%, var(--gold-deep)); -webkit-background-clip: text; background-clip: text; color: transparent; }
  .earth-role { left: 451px; top: 167px; font-size: 14px; }
  .earth-levels { position: absolute; left: 338px; top: 197px; list-style: none; }
  .earth-levels li { height: 22px; display: flex; align-items: baseline; font-size: 11.5px; white-space: nowrap; }
  .earth-levels .lvl { width: 65px; font-family: "Cinzel", serif; font-size: 12px; color: var(--gold); }
  .earth-levels b { font-weight: 700; }

  .wind-name { left: 338px; top: 393px; font-size: 31px; background: linear-gradient(180deg, #ffffff 0%, #d8d8d8 45%, #6e6e6e 55%, #bdbdbd 100%); -webkit-background-clip: text; background-clip: text; color: transparent; }
  .wind-role { left: 467px; top: 398px; font-size: 17px; }

  .fire-name { left: 196px; top: 535px; font-size: 32px; color: var(--fire); }
  .fire-role { left: 291px; top: 543px; font-size: 13px; }
  .water-name { left: 196px; top: 805px; font-size: 32px; color: #23279a; }
  .water-role { left: 340px; top: 813px; font-size: 13px; }

  .level-label { position: absolute; width: 120px; text-align: center; }
  .level-label .lvl { display: block; font-family: "Cinzel", serif; font-size: 14px; letter-spacing: 0.5px; line-height: 1; }
  .level-label .count { display: block; margin-top: 8px; font-weight: 700; font-size: 11px; line-height: 1.1; }
  .level-label .unit { display: block; font-size: 12px; letter-spacing: 0.3px; line-height: 1.2; }
  .fire-row .lvl { color: var(--fire-text); }
  .water-row .lvl { color: var(--water-text); }

  .footer-line { position: absolute; height: 1px; background: linear-gradient(90deg, rgba(200,150,60,0), #b8892e 20%, #b8892e 80%, rgba(200,150,60,0)); }
  .footer-mark { position: absolute; left: 346px; top: 1068px; width: 108px; height: 110px; background: #000; display: flex; flex-direction: column; align-items: center; justify-content: center; gap: 8px; }
  .footer-dot { width: 34px; height: 34px; border-radius: 50%; background: var(--gold); }
  .footer-name { font-family: "Montserrat", sans-serif; font-weight: 700; font-size: 8px; letter-spacing: 1px; text-align: center; color: var(--white); line-height: 1.2; }
</style>
</head>
<body>
<svg width="0" height="0" style="position:absolute" aria-hidden="true">
  <defs>
    <linearGradient id="g-gold" x1="0" y1="0" x2="1" y2="1">
      <stop offset="0" stop-color="#f8e29a"/><stop offset="0.5" stop-color="#e0a23a"/><stop offset="1" stop-color="#c66f1c"/>
    </linearGradient>
    <linearGradient id="g-silver" x1="0" y1="0" x2="1" y2="1">
      <stop offset="0" stop-color="#ffffff"/><stop offset="0.35" stop-color="#bdbdbd"/><stop offset="0.55" stop-color="#5e5e5e"/><stop offset="0.8" stop-color="#e6e6e6"/><stop offset="1" stop-color="#8a8a8a"/>
    </linearGradient>
    <linearGradient id="g-dark" x1="0" y1="0" x2="1" y2="1">
      <stop offset="0" stop-color="#6a6a6a"/><stop offset="0.5" stop-color="#2a2a2a"/><stop offset="1" stop-color="#5a5a5a"/>
    </linearGradient>
    <radialGradient id="g-fire" cx="0.5" cy="0.4" r="0.6">
      <stop offset="0" stop-color="#c41a14"/><stop offset="1" stop-color="#5e0606"/>
    </radialGradient>
    <radialGradient id="g-water" cx="0.5" cy="0.4" r="0.6">
      <stop offset="0" stop-color="#2c32a6"/><stop offset="1" stop-color="#141764"/>
    </radialGradient>
    <linearGradient id="g-wind-face" x1="0" y1="0" x2="1" y2="1">
      <stop offset="0" stop-color="#ffffff"/><stop offset="0.5" stop-color="#d6d6d6"/><stop offset="1" stop-color="#9a9a9a"/>
    </linearGradient>
  </defs>
</svg>

<main class="canvas">
  <p class="tagline">SERVE BEYOND YOURSELF</p>
  <h1 class="title">KESTREL LEADERSHIP HIERCHY</h1>

  <div class="timeline"></div>
  <div class="node" style="top:218px"><span class="node-num">04</span><span class="node-diamond"></span><span class="node-tick"></span></div>
  <div class="node" style="top:408px"><span class="node-num">03</span><span class="node-diamond"></span><span class="node-tick"></span></div>
  <div class="node" style="top:641px"><span class="node-num">02</span><span class="node-diamond"></span><span class="node-tick"></span></div>
  <div class="node" style="top:900px"><span class="node-num">01</span><span class="node-diamond"></span><span class="node-tick"></span></div>

  <!-- Earth -->
  <section class="tier tier-earth">
    <div class="badge" style="left:195px;top:150px;width:124px;height:143px">
      <svg viewBox="0 0 100 115">
        <polygon points="50,0 100,28.75 100,86.25 50,115 0,86.25 0,28.75" fill="url(#g-gold)"/>
        <polygon points="50,9 92,33 92,82 50,106 8,82 8,33" fill="#000"/>
        <polygon points="50,14 87,35.5 87,79.5 50,101 13,79.5 13,35.5" fill="none" stroke="url(#g-gold)" stroke-width="1.5"/>
        <circle cx="50" cy="57.5" r="21" fill="none" stroke="url(#g-gold)" stroke-width="2.5"/>
        <circle cx="50" cy="57.5" r="15" fill="url(#g-gold)" role="img" aria-label="Earth element symbol"/>
      </svg>
    </div>
    <h2 class="tier-name earth-name">EARTH</h2>
    <span class="tier-role earth-role">(TOP LEADERSHIP)</span>
    <ul class="earth-levels">
      <li><span class="lvl">LEVEL 1</span><span><b>200</b> Active Student + <b>3</b> Element Instructors</span></li>
      <li><span class="lvl">LEVEL 2</span><span><b>350</b> Active Student + <b>6</b> Element Instructors</span></li>
      <li><span class="lvl">LEVEL 3</span><span><b>500</b> Active Student + <b>9</b> Element Instructors</span></li>
      <li><span class="lvl">LEVEL 4</span><span><b>1000</b> Active Student + <b>18</b> Element Instructors</span></li>
    </ul>
  </section>
  <div class="rule" style="top:324px"></div>

  <!-- Wind -->
  <section class="tier tier-wind">
    <div class="badge" style="left:195px;top:350px;width:107px;height:123px">
      <svg viewBox="0 0 100 115">
        <polygon points="50,0 100,28.75 100,86.25 50,115 0,86.25 0,28.75" fill="url(#g-silver)"/>
        <polygon points="50,8 93,32.5 93,82.5 50,107 7,82.5 7,32.5" fill="#0a0a0a"/>
        <polygon points="50,13 88.5,35 88.5,80 50,102 11.5,80 11.5,35" fill="url(#g-wind-face)"/>
        <circle cx="50" cy="57.5" r="21" fill="#fff" stroke="#0a0a0a" stroke-width="2.5"/>
        <circle cx="50" cy="57.5" r="13" fill="#0a0a0a" role="img" aria-label="Wind element symbol"/>
      </svg>
    </div>
    <h2 class="tier-name wind-name">WIND</h2>
    <span class="tier-role wind-role">(LEAD INSTRUCTOR)</span>
  </section>
  <div class="rule" style="top:500px"></div>

  <!-- Fire -->
  <section class="tier tier-fire fire-row">
    <h2 class="tier-name fire-name">FIRE</h2>
    <span class="tier-role fire-role">(CHIEF INSTRUCTOR)</span>

    <div class="badge" style="left:194px;top:592px;width:86px;height:99px">
      <svg viewBox="0 0 100 115">
        <polygon points="50,0 100,28.75 100,86.25 50,115 0,86.25 0,28.75" fill="#fff"/>
        <polygon points="50,10 91,33.5 91,81.5 50,105 9,81.5 9,33.5" fill="#000"/>
        <polygon points="50,15 86.5,36 86.5,79 50,100 13.5,79 13.5,36" fill="url(#g-fire)"/>
        <circle cx="50" cy="57.5" r="20" fill="none" stroke="#fff" stroke-width="3"/>
        <circle cx="50" cy="57.5" r="12" fill="#fff" role="img" aria-label="Fire element symbol"/>
      </svg>
    </div>
    <div class="badge" style="left:325px;top:592px;width:86px;height:99px">
      <svg viewBox="0 0 100 115">
        <polygon points="50,0 100,28.75 100,86.25 50,115 0,86.25 0,28.75" fill="url(#g-dark)"/>
        <polygon points="50,10 91,33.5 91,81.5 50,105 9,81.5 9,33.5" fill="#000"/>
        <polygon points="50,15 86.5,36 86.5,79 50,100 13.5,79 13.5,36" fill="url(#g-fire)"/>
        <circle cx="50" cy="57.5" r="20" fill="none" stroke="#3a3a3a" stroke-width="3"/>
        <circle cx="50" cy="57.5" r="12" fill="#2a2a2a" role="img" aria-label="Fire element symbol"/>
      </svg>
    </div>
    <div class="badge" style="left:456px;top:592px;width:86px;height:99px">
      <svg viewBox="0 0 100 115">
        <polygon points="50,0 100,28.75 100,86.25 50,115 0,86.25 0,28.75" fill="url(#g-silver)"/>
        <polygon points="50,10 91,33.5 91,81.5 50,105 9,81.5 9,33.5" fill="#000"/>
        <polygon points="50,15 86.5,36 86.5,79 50,100 13.5,79 13.5,36" fill="url(#g-fire)"/>
        <circle cx="50" cy="57.5" r="20" fill="none" stroke="url(#g-silver)" stroke-width="3"/>
        <circle cx="50" cy="57.5" r="12" fill="url(#g-silver)" role="img" aria-label="Fire element symbol"/>
      </svg>
    </div>
    <div class="badge" style="left:588px;top:592px;width:86px;height:99px">
      <svg viewBox="0 0 100 115">
        <polygon points="50,0 100,28.75 100,86.25 50,115 0,86.25 0,28.75" fill="url(#g-silver)"/>
        <polygon points="50,10 91,33.5 91,81.5 50,105 9,81.5 9,33.5" fill="#000"/>
        <polygon points="50,15 86.5,36 86.5,79 50,100 13.5,79 13.5,36" fill="url(#g-fire)"/>
        <circle cx="50" cy="57.5" r="20" fill="none" stroke="url(#g-silver)" stroke-width="3"/>
        <circle cx="50" cy="57.5" r="12" fill="url(#g-silver)" role="img" aria-label="Fire element symbol"/>
      </svg>
    </div>

    <div class="level-label" style="left:175px;top:705px"><span class="lvl">LEVEL 1</span><span class="count">50</span><span class="unit">Active Student</span></div>
    <div class="level-label" style="left:308px;top:705px"><span class="lvl">LEVEL 2</span><span class="count">100</span><span class="unit">Active Student</span></div>
    <div class="level-label" style="left:442px;top:705px"><span class="lvl">LEVEL 3</span><span class="count">150</span><span class="unit">Active Student</span></div>
    <div class="level-label" style="left:570px;top:705px"><span class="lvl">LEVEL 4</span><span class="count">200</span><span class="unit">Active Student</span></div>
  </section>
  <div class="rule" style="top:780px"></div>

  <!-- Water -->
  <section class="tier tier-water water-row">
    <h2 class="tier-name water-name">WATER</h2>
    <span class="tier-role water-role">(PROGRAM DIRECTOR)</span>

    <div class="badge" style="left:196px;top:852px;width:82px;height:95px">
      <svg viewBox="0 0 100 115">
        <polygon points="50,0 100,28.75 100,86.25 50,115 0,86.25 0,28.75" fill="#fff"/>
        <polygon points="50,10 91,33.5 91,81.5 50,105 9,81.5 9,33.5" fill="#000"/>
        <polygon points="50,15 86.5,36 86.5,79 50,100 13.5,79 13.5,36" fill="url(#g-water)"/>
        <circle cx="50" cy="57.5" r="20" fill="none" stroke="#fff" stroke-width="3"/>
        <circle cx="50" cy="57.5" r="12" fill="#fff" role="img" aria-label="Water element symbol"/>
      </svg>
    </div>
    <div class="badge" style="left:327px;top:852px;width:82px;height:95px">
      <svg viewBox="0 0 100 115">
        <polygon points="50,0 100,28.75 100,86.25 50,115 0,86.25 0,28.75" fill="url(#g-dark)"/>
        <polygon points="50,10 91,33.5 91,81.5 50,105 9,81.5 9,33.5" fill="#000"/>
        <polygon points="50,15 86.5,36 86.5,79 50,100 13.5,79 13.5,36" fill="url(#g-water)"/>
        <circle cx="50" cy="57.5" r="20" fill="none" stroke="#3a3a3a" stroke-width="3"/>
        <circle cx="50" cy="57.5" r="12" fill="#2a2a2a" role="img" aria-label="Water element symbol"/>
      </svg>
    </div>
    <div class="badge" style="left:458px;top:852px;width:82px;height:95px">
      <svg viewBox="0 0 100 115">
        <polygon points="50,0 100,28.75 100,86.25 50,115 0,86.25 0,28.75" fill="url(#g-silver)"/>
        <polygon points="50,10 91,33.5 91,81.5 50,105 9,81.5 9,33.5" fill="#000"/>
        <polygon points="50,15 86.5,36 86.5,79 50,100 13.5,79 13.5,36" fill="url(#g-water)"/>
        <circle cx="50" cy="57.5" r="20" fill="none" stroke="url(#g-silver)" stroke-width="3"/>
        <circle cx="50" cy="57.5" r="12" fill="url(#g-silver)" role="img" aria-label="Water element symbol"/>
      </svg>
    </div>
    <div class="badge" style="left:590px;top:852px;width:82px;height:95px">
      <svg viewBox="0 0 100 115">
        <polygon points="50,0 100,28.75 100,86.25 50,115 0,86.25 0,28.75" fill="url(#g-silver)"/>
        <polygon points="50,10 91,33.5 91,81.5 50,105 9,81.5 9,33.5" fill="#000"/>
        <polygon points="50,15 86.5,36 86.5,79 50,100 13.5,79 13.5,36" fill="url(#g-water)"/>
        <circle cx="50" cy="57.5" r="20" fill="none" stroke="url(#g-silver)" stroke-width="3"/>
        <circle cx="50" cy="57.5" r="12" fill="url(#g-silver)" role="img" aria-label="Water element symbol"/>
      </svg>
    </div>

    <div class="level-label" style="left:175px;top:964px"><span class="lvl">LEVEL 1</span><span class="count">50</span><span class="unit">Active Student</span></div>
    <div class="level-label" style="left:308px;top:964px"><span class="lvl">LEVEL 2</span><span class="count">100</span><span class="unit">Active Student</span></div>
    <div class="level-label" style="left:442px;top:964px"><span class="lvl">LEVEL 3</span><span class="count">150</span><span class="unit">Active Student</span></div>
    <div class="level-label" style="left:570px;top:964px"><span class="lvl">LEVEL 4</span><span class="count">200</span><span class="unit">Active Student</span></div>
  </section>

  <!-- Footer -->
  <footer>
    <div class="footer-line" style="left:0;top:1102px;width:800px"></div>
    <div class="footer-line" style="left:59px;top:1136px;width:681px"></div>
    <div class="footer-mark">
      <span class="footer-dot"></span>
      <span class="footer-name">IGNITE<br>KESTREL PATH</span>
    </div>
  </footer>
</main>
</body>
</html>
```